ALL TEXT Social Media Graphics

We are looking for a series of social media graphics for Instagram (new size: 4:5 (1080 x 1350 pixels) ratio that are ALL TEXT. We want the following quotes below on each graphic; one quote per graphic. AND, In very small letters at the bottom of each graphic, add @KPBrandellLive
The look and feel of these graphics should be complimentary to the color palette attached below; but keep them simple. But the design is up to you; at the end of this document, I provided various samples of all text graphics that I like as examples.
The Quotes are in the attached WORD document
Target Market(s)
women trying to lose weight
Look and feel
Each slider illustrates characteristics of the customer's brand and the style your logo design should communicate.

```html
<!DOCTYPE html>
<html lang="en">
<head>
<meta charset="utf-8">
<title>Glow Girl Summer Shapeup – Social Graphics</title>
<link href="https://fonts.googleapis.com/css2?family=Barlow+Condensed:wght@700;800&family=Barlow+Semi+Condensed:wght@300&family=Barlow:wght@400&display=swap" rel="stylesheet">
<style>
  :root {
    --backdrop: #d9b8cb;
    --card: #ffffff;
    --magenta: #b3185d;
    --pink: #ec6c9f;
  }
  * { box-sizing: border-box; margin: 0; padding: 0; }
  html, body {
    width: 732px;
    height: 1200px;
    overflow: hidden;
    background: var(--backdrop);
  }
  .board {
    position: relative;
    width: 732px;
    height: 1200px;
  }
  .post {
    position: absolute;
    width: 210px;
    height: 263px;
    background: var(--card);
    padding: 12px 6px 0 7px;
    white-space: nowrap;
    overflow: hidden;
  }
  .col-1 { left: 22px; }
  .col-2 { left: 261px; }
  .col-3 { left: 500px; }
  .row-1 { top: 31px; }
  .row-2 { top: 323px; }
  .row-3 { top: 615px; }
  .row-4 { top: 907px; }

  .headline {
    font-family: "Barlow Condensed", sans-serif;
    font-weight: 700;
    font-size: 22px;
    line-height: 27.3px;
    letter-spacing: -0.2px;
    color: var(--magenta);
    text-transform: uppercase;
  }
  .headline .heavy { font-weight: 800; }
  .headline--airy { line-height: 31.5px; }
  .subline {
    font-family: "Barlow Semi Condensed", sans-serif;
    font-weight: 300;
    font-size: 22px;
    line-height: 27.3px;
    letter-spacing: 0.1px;
    color: var(--pink);
    text-transform: uppercase;
    margin-top: 6px;
  }
  .subline--spaced { margin-top: 15px; }
  .subline--inset { margin-left: 3px; }
  .call {
    font-family: "Barlow", sans-serif;
    font-weight: 400;
    font-size: 15.5px;
    line-height: 19.4px;
    color: var(--magenta);
    text-transform: uppercase;
    margin-top: 4px;
  }
  .call--spaced { margin-top: 14px; }
  .call--tight { margin-top: 0; }
  .call--loose { line-height: 22.5px; margin-top: 30px; }
  .call--far { margin-top: 38px; }
  .call .keyword { color: var(--pink); }
  .handle {
    position: absolute;
    left: 0;
    right: 0;
    bottom: 11px;
    text-align: center;
    font-family: "Barlow", sans-serif;
    font-size: 6px;
    color: var(--magenta);
  }
</style>
</head>
<body>
<main class="board">

  <section class="post col-1 row-1">
    <h2 class="headline">You can absolutely<br>be down <span class="heavy">20–30</span> pounds<br>by end of summer.</h2>
    <p class="subline">All it takes is the<br>right plan—and<br>you’ve found it.</p>
    <p class="call">Comment <span class="keyword">“Glow Girl”</span><br>for the Glow Girl<br>Summer Shapeup!</p>
    <p class="handle">@KPBrandellLive</p>
  </section>

  <section class="post col-2 row-1">
    <h2 class="headline">You don’t need<br>another diet—you need<br>a system that works.</h2>
    <p class="subline subline--spaced">Drop 30 pounds<br>with the Glow Girl<br>Summer Shapeup.</p>
    <p class="call call--spaced">Comment <span class="keyword">“Summer”</span><br>to start now.</p>
    <p class="handle">@KPBrandellLive</p>
  </section>

  <section class="post col-3 row-1">
    <h2 class="headline">This summer ain’t<br>over—and neither<br>are your body goals.</h2>
    <p class="subline subline--spaced">Drop 30 pounds with<br>the Glow Girl<br>Summer Shapeup.</p>
    <p class="call call--spaced">Comment <span class="keyword">“Glow Girl”</span><br>to get the plan.</p>
    <p class="handle">@KPBrandellLive</p>
  </section>

  <section class="post col-1 row-2">
    <h2 class="headline headline--airy">If your goal is a<br>tiny waist, flat belly,<br>and 30 pounds<br>down—this is the plan.</h2>
    <p class="call call--loose">Comment <span class="keyword">“Summer”</span> to<br>join the Glow Girl<br>Summer Shapeup!</p>
    <p class="handle">@KPBrandellLive</p>
  </section>

  <section class="post col-2 row-2">
    <h2 class="headline">There’s still time<br>to drop the<br>30 pounds and slay<br>this summer.</h2>
    <p class="subline subline--inset">The Glow Girl<br>Summer Shapeup has<br>the blueprint.</p>
    <p class="call">Comment <span class="keyword">“Glow Girl”</span>!</p>
    <p class="handle">@KPBrandellLive</p>
  </section>

  <section class="post col-3 row-2">
    <h2 class="headline">Snatched waist,<br>flat tummy,<br>30 pounds lighter<br>that’s what the<br>Glow Girl Summer<br>Shapeup Challenge<br>delivers.</h2>
    <p class="call call--tight">Comment <span class="keyword">“Glow Girl”</span><br>to get the plan</p>
    <p class="handle">@KPBrandellLive</p>
  </section>

  <section class="post col-1 row-3">
    <h2 class="headline">Nothing feels better<br>than seeing that scale<br>drop week after week.</h2>
    <p class="subline">Let’s lose up to<br>30 pounds this<br>summer—together.</p>
    <p class="call">Comment <span class="keyword">“Summer”</span> to<br>join the Glow Girl<br>Summer Shapeup!</p>
    <p class="handle">@KPBrandellLive</p>
  </section>

  <section class="post col-2 row-3">
    <h2 class="headline headline--airy">Sis, we’re dropping<br>belly flat and<br>saying goodbye<br>to stubborn pounds.</h2>
    <p class="call call--far">Oin the Glow Girl Summer<br>Shapeup—comment<br><span class="keyword">“Summer”</span>!</p>
    <p class="handle">@KPBrandellLive</p>
  </section>

  <section class="post col-3 row-3">
    <h2 class="headline">Don’t wait ‘til next<br>summer to get right.</h2>
    <p class="subline">The time is now.<br>Drop 30 pounds<br>with the Glow Girl<br>Summer Shapeup.</p>
    <p class="call call--tight">Comment <span class="keyword">“Summer”</span>!</p>
    <p class="handle">@KPBrandellLive</p>
  </section>

  <section class="post col-1 row-4">
    <h2 class="headline">You’ve got 8 weeks<br>and the perfect plan<br>to drop 30 pounds.</h2>
    <p class="subline">Let’s get snatched<br>this summer with<br>the Glow Girl<br>Summer Shapeup.</p>
    <p class="call">Comment <span class="keyword">“Summer”</span>!</p>
    <p class="handle">@KPBrandellLive</p>
  </section>

</main>
</body>
</html>
```